A new presentation to our clients

we are a Real Estate agency, our website is www.lirotama.com and it’s time to have a new, fashion and remarcable Business Card. we want to differentiate ourselves from other companies so we want a business card that differentiates us. we want the business card to impact our customers. in the competitive market that we have today, we have to be different and it is this difference that we seek

Target Market(s)

Real Estate Clients

Contact Information for Business Card

We search a totaly diferent card from the usual

Font styles to use
Sans Serif

Colors
e34197

Requirements
Must have
• Logo, adress, phone contact, e-mail, photo, and our website
Nice to have
• We would like to see a modern business card
Should not have
• Houses or building draws

```html
<!DOCTYPE html>
<html lang="en">
<head>
<meta charset="utf-8">
<title>Lirotama Business Card</title>
<link rel="stylesheet" href="https://fonts.googleapis.com/css2?family=Poppins:wght@300;400;600;700&display=swap">
<style>
  :root {
    --brand-pink: #e0195f;
    --brand-pink-light: #e34197;
    --paper: #f4f4f4;
    --ink: #3a3a3a;
    --charcoal: #4a4a4a;
    --backdrop: #8fa7ae;
    --photo-top: #c9d6e2;
    --photo-bottom: #5d7aa0;
  }
  * { margin: 0; padding: 0; box-sizing: border-box; }
  html, body { width: 1200px; height: 1200px; overflow: hidden; }
  body {
    background: var(--backdrop);
    font-family: "Poppins", sans-serif;
    position: relative;
  }
  .business-card {
    position: absolute;
    left: 100px; top: 315px;
    width: 1000px; height: 570px;
    background: var(--paper);
    border-radius: 6px;
    overflow: hidden;
    box-shadow: 0 18px 40px rgba(0,0,0,0.18);
  }
  .base-strip {
    position: absolute; left: 150px; bottom: 0;
    width: 850px; height: 80px;
    background: var(--charcoal);
    border-top-left-radius: 40px;
  }
  .base-cover {
    position: absolute; left: 0; bottom: 36px;
    width: 960px; height: 70px;
    background: var(--paper);
    border-bottom-right-radius: 40px;
  }
  .top-band {
    position: absolute; left: 0; top: 0;
    width: 100%; height: 150px;
    background: linear-gradient(90deg, var(--brand-pink) 0%, var(--brand-pink-light) 100%);
  }
  .side-block {
    position: absolute; left: 0; top: 0;
    width: 290px; height: 320px;
    background: var(--brand-pink);
    border-bottom-right-radius: 50px;
  }
  .content-panel {
    position: absolute; left: 290px; top: 150px;
    width: 710px; height: 300px;
    background: var(--paper);
    border-top-left-radius: 60px;
  }
  .brand-name {
    position: absolute; left: 260px; top: 42px;
    color: #fff;
    font-weight: 600;
    font-size: 62px;
    letter-spacing: 1px;
    line-height: 1;
  }
  .portrait {
    position: absolute; left: 180px; top: 195px;
    width: 230px; height: 230px;
    border-radius: 50%;
    background: var(--paper);
    padding: 10px;
  }
  .portrait-fill {
    width: 100%; height: 100%;
    border-radius: 50%;
    border: 4px solid var(--brand-pink);
    background: linear-gradient(170deg, var(--photo-top) 0%, var(--photo-bottom) 100%);
  }
  .person-name {
    position: absolute; left: 440px; top: 172px;
    color: var(--brand-pink);
    font-weight: 700;
    font-size: 52px;
    line-height: 1;
  }
  .person-role {
    position: absolute; left: 462px; top: 238px;
    color: var(--ink);
    font-weight: 300;
    font-size: 38px;
    line-height: 1;
  }
  .contact {
    position: absolute;
    display: flex; align-items: center; gap: 16px;
    color: var(--ink);
    font-size: 26px;
    font-weight: 400;
    line-height: 40px;
  }
  .contact svg { width: 40px; height: 40px; flex: none; }
  .contact--mail { left: 620px; top: 320px; }
  .contact--web { left: 620px; top: 374px; }
  .contact--phone { left: 250px; top: 436px; }
  .contact--fax { left: 250px; top: 484px; }
</style>
</head>
<body>
  <div class="business-card">
    <div class="base-strip"></div>
    <div class="base-cover"></div>
    <div class="top-band"></div>
    <div class="side-block"></div>
    <div class="content-panel"></div>

    <div class="brand-name">Lirotama</div>

    <div class="portrait">
      <div class="portrait-fill" role="img" aria-label="Portrait photo of the agent in a suit"></div>
    </div>

    <div class="person-name">Your Name</div>
    <div class="person-role">Your Designation</div>

    <div class="contact contact--mail">
      <svg viewBox="0 0 40 40" aria-hidden="true">
        <circle cx="20" cy="20" r="20" fill="var(--brand-pink)"/>
        <rect x="10" y="13" width="20" height="14" rx="2" fill="none" stroke="#fff" stroke-width="2.4"/>
        <path d="M10 14 L20 22 L30 14" fill="none" stroke="#fff" stroke-width="2.4"/>
      </svg>
      <span>geral@lirotama.com</span>
    </div>
    <div class="contact contact--web">
      <svg viewBox="0 0 40 40" aria-hidden="true">
        <circle cx="20" cy="20" r="20" fill="var(--brand-pink)"/>
        <circle cx="20" cy="20" r="10" fill="none" stroke="#fff" stroke-width="2.2"/>
        <ellipse cx="20" cy="20" rx="4.5" ry="10" fill="none" stroke="#fff" stroke-width="2"/>
        <path d="M10 20 H30 M12 15 H28 M12 25 H28" stroke="#fff" stroke-width="1.8"/>
      </svg>
      <span>www.lirotama.com</span>
    </div>
    <div class="contact contact--phone">
      <svg viewBox="0 0 40 40" aria-hidden="true">
        <circle cx="20" cy="20" r="20" fill="var(--brand-pink)"/>
        <path d="M11 23 Q20 15 29 23 L26 27 L23 24 Q20 22 17 24 L14 27 Z" fill="#fff"/>
        <path d="M15 15 Q20 11 25 15" fill="none" stroke="#fff" stroke-width="2"/>
      </svg>
      <span>(+351) 210 458 170</span>
    </div>
    <div class="contact contact--fax">
      <svg viewBox="0 0 40 40" aria-hidden="true">
        <circle cx="20" cy="20" r="20" fill="var(--brand-pink)"/>
        <rect x="14" y="10" width="12" height="7" fill="none" stroke="#fff" stroke-width="2"/>
        <rect x="10" y="17" width="20" height="10" rx="2" fill="#fff"/>
        <rect x="14" y="24" width="12" height="7" fill="#fff" stroke="var(--brand-pink)" stroke-width="1.5"/>
      </svg>
      <span>(+351) 210 458 179</span>
    </div>
  </div>
</body>
</html>
```